business card for law firm that reflects the web site -www.MarenHolt.com. That is pleasant to read

We need a business card for a small law firm. Your company designed our logo - tree of life - which I can provide to the designers. The card should be on both sides. Use the coloring from the web site (www.MarenHolt.com) and logo (I have several formats). I am attaching the logo, but not sure what format to use.

First side name of firm: Law Office of M.K. Holt, P.A. 4816 West Sorrelwood, Suite 300, Phoenix, AZ 85019, Phone: 602.555.0143, Fax: 602.555.0187, web site: www.MarenHolt.com, email: MHolt@MarenHolt.com.
Maren K. Holt Bankruptcy and Foreclosure Attorney & Counselor.
Back side (perhaps vertical) the logo and then Notes with lines. At the bottom: Proud to help people and small businesses file for bankruptcy protection. We are a debt relief agency.
Updates

I have several versions of the logo. Will be happy to share whatever you need. Added Sunday, April 3, 2016

Target Market(s)

everyone

Industry/Entity Type

Legal

Contact Information for Business Card

I prefer something unique (rounded edges, design that adopts my web site - www.MarenHolt.com.

Font styles to use
Serif

Requirements
Must have
• First side name of firm: Law Office of M.K. Holt, P.A. 4816 West Sorrelwood, Suite 300, Phoenix, AZ 85019, Phone: 602.555.0143, Fax: 602.555.0187, web site: www.MarenHolt.com, email: MHolt@MarenHolt.com.
• Maren K. Holt Bankruptcy and Foreclosure Attorney & Counselor.
• Back side (perhaps vertical) the logo and then Notes with lines. At the bottom: Proud to help people and small businesses file for bankruptcy protection. We are a debt relief agency.
• Green and brown colors that reflect the web site: www.MarenHolt.com
Should not have
• Type so small that older people cannot read.

```html
<!DOCTYPE html>
<html lang="en">
<head>
<meta charset="utf-8">
<title>Law Office of M.K. Holt, P.A. — Business Card</title>
<link rel="stylesheet" href="https://fonts.googleapis.com/css2?family=Merriweather:wght@700&family=Open+Sans:ital,wght@0,400;1,400&family=Vollkorn:wght@500&display=swap">
<style>
  :root{
    --backdrop:#ecebe7;
    --card:#ffffff;
    --bar-brown:#33200f;
    --band-green:#1d3620;
    --name-green:#1f3d24;
    --firm-brown:#3a2212;
    --body-gray:#555555;
    --rule-gray:#d6d6d6;
    --icon-dark:#333333;
  }
  *{box-sizing:border-box;margin:0;padding:0}
  html,body{width:1200px;height:1000px;overflow:hidden}
  body{background:var(--backdrop);position:relative;font-family:"Open Sans",Arial,sans-serif}

  .card{position:absolute;background:var(--card);border-radius:14px;overflow:hidden;box-shadow:0 4px 14px rgba(0,0,0,.18)}
  .card__topbar{position:absolute;left:0;top:0;width:100%;background:var(--bar-brown)}
  .card__band{position:absolute;left:0;bottom:0;width:100%;background:var(--band-green);color:#fff;display:flex;align-items:center;justify-content:center;text-align:center;z-index:2}

  .brand-mark{position:absolute;display:flex;align-items:center;justify-content:center;border-radius:50%;border:6px solid var(--firm-brown)}
  .brand-mark__name{font-family:"Merriweather",Georgia,serif;font-weight:700;color:var(--firm-brown);white-space:nowrap}

  /* back side */
  .card--back{left:50px;top:92px;width:466px;height:816px}
  .card--back .card__topbar{height:22px}
  .card--back .brand-mark{left:110px;top:48px;width:240px;height:240px}
  .card--back .brand-mark__name{font-size:28px}
  .back__url{position:absolute;left:0;width:460px;top:306px;text-align:center;font-size:18px;color:var(--body-gray)}
  .notes{position:absolute;left:38px;top:422px;right:38px}
  .notes__label{font-family:"Merriweather",Georgia,serif;font-weight:700;font-size:22px;color:var(--firm-brown)}
  .notes__line{height:1px;background:var(--rule-gray);margin-top:52px}
  .notes__line:first-of-type{margin-top:10px}
  .card--back .card__band{height:86px;font-style:italic;font-size:16px;line-height:1.45;padding:0 50px}

  /* front side */
  .card--front{left:306px;top:300px;width:846px;height:481px}
  .card--front .card__topbar{height:24px}
  .card--front .brand-mark{left:42px;top:105px;width:270px;height:270px}
  .card--front .brand-mark__name{font-size:32px}
  .front__divider{position:absolute;left:331px;top:80px;width:1px;height:290px;background:var(--rule-gray)}
  .front__details{position:absolute;left:351px;top:78px;z-index:1}
  .attorney__name{font-family:"Vollkorn",Georgia,serif;font-weight:500;font-size:31px;letter-spacing:1.5px;text-transform:uppercase;color:var(--name-green);line-height:1.1}
  .attorney__title{font-size:16.5px;color:var(--body-gray);margin-top:4px}
  .firm__name{font-family:"Merriweather",Georgia,serif;font-weight:700;font-size:22px;text-transform:uppercase;color:var(--firm-brown);margin-top:16px;letter-spacing:.3px;white-space:nowrap}
  .firm__address{font-size:19.5px;color:var(--body-gray);line-height:1.45;margin-top:0}
  .contact-list{list-style:none;margin-top:8px}
  .contact-list li{display:flex;align-items:center;gap:9px;font-size:19.5px;color:var(--body-gray);height:30.5px}
  .contact-list svg{width:17px;height:17px;fill:var(--icon-dark)}
  .tree-art{position:absolute;right:0;top:195px;width:166px;height:238px;background:radial-gradient(ellipse at 55% 40%,#2e5431 0%,#1f3d24 50%,rgba(31,61,36,0) 75%)}
  .card--front .card__band{height:48px;font-size:19px;text-transform:uppercase;letter-spacing:.3px}
</style>
</head>
<body>

<section class="card card--back" aria-label="Card back">
  <div class="card__topbar"></div>
  <div class="brand-mark"><span class="brand-mark__name">M.K. Holt</span></div>
  <p class="back__url">www.MarenHolt.com</p>
  <div class="notes">
    <p class="notes__label">Notes:</p>
    <div class="notes__line"></div>
    <div class="notes__line"></div>
    <div class="notes__line"></div>
    <div class="notes__line"></div>
  </div>
  <div class="card__band">Proud to help people and small businesses file for bankruptcy protection.</div>
</section>

<section class="card card--front" aria-label="Card front">
  <div class="card__topbar"></div>
  <div class="brand-mark"><span class="brand-mark__name">M.K. Holt</span></div>
  <div class="front__divider"></div>
  <div class="tree-art" role="img" aria-label="Dark green leafy tree illustration"></div>
  <div class="front__details">
    <h1 class="attorney__name">Maren K. Holt</h1>
    <p class="attorney__title">Bankruptcy and Foreclosure Attorney &amp; Counselor</p>
    <h2 class="firm__name">Law Office of M.K. Holt, P.A.</h2>
    <p class="firm__address">4816 West Sorrelwood, Suite 300<br>Phoenix, AZ 85019</p>
    <ul class="contact-list">
      <li><svg viewBox="0 0 24 24" aria-hidden="true"><path d="M6.6 10.8a15.1 15.1 0 0 0 6.6 6.6l2.2-2.2c.3-.3.7-.4 1-.2 1.1.4 2.3.6 3.6.6.6 0 1 .4 1 1V20c0 .6-.4 1-1 1C10.6 21 3 13.4 3 4c0-.6.4-1 1-1h3.5c.6 0 1 .4 1 1 0 1.3.2 2.5.6 3.6.1.3 0 .7-.2 1z"/></svg>602.555.0143</li>
      <li><svg viewBox="0 0 24 24" aria-hidden="true"><path d="M6 2h12v5H6zM4 8h16a2 2 0 0 1 2 2v7h-4v5H6v-5H2v-7a2 2 0 0 1 2-2zm4 8v4h8v-4z"/></svg>602.555.0187</li>
      <li><svg viewBox="0 0 24 24" aria-hidden="true"><path d="M2 5h20v14H2zm2 2v.5l8 5.5 8-5.5V7zm0 2.9V17h16V9.9l-8 5.5z"/></svg>MHolt@MarenHolt.com</li>
      <li><svg viewBox="0 0 24 24" aria-hidden="true"><path d="M12 2a10 10 0 1 0 0 20 10 10 0 0 0 0-20zm6.9 9h-3a15 15 0 0 0-1.3-6.1A8 8 0 0 1 18.9 11zM12 4.1c.9 1.2 1.8 3.6 1.9 6.9h-3.8c.1-3.3 1-5.7 1.9-6.9zM9.4 4.9A15 15 0 0 0 8.1 11h-3a8 8 0 0 1 4.3-6.1zM5.1 13h3a15 15 0 0 0 1.3 6.1A8 8 0 0 1 5.1 13zm6.9 6.9c-.9-1.2-1.8-3.6-1.9-6.9h3.8c-.1 3.3-1 5.7-1.9 6.9zm2.6-.8a15 15 0 0 0 1.3-6.1h3a8 8 0 0 1-4.3 6.1z"/></svg>www.MarenHolt.com</li>
    </ul>
  </div>
  <div class="card__band">Helping you get your life back on track</div>
</section>

</body>
</html>
```